App Design

This is a 'video player' app - will be used to stream video files and watch them on a device. Need 3/4 skins for user customization.
Design will need to be versatile - used on: Kestrel4/4S/5 and vexTab2/3
Require an app design that shows the required functionality described by us, allows ease to navigate and visually creates a unique user experience.
App must have following pages: (refer to attached pages)
1. Search Page
2. Results Page
3. Video Page
4. End Page
3-4 skins for user preference
important: if you are interested please submit designs by tomorrow night - we will be picking from submitted designs - will make revisions and finalize the design within 4-5 days.
timing is crucial- please only submit if you can commit to timeline and design requirements. There will be refinements required.
Please see the attached update.
Additional reference files have been added to help in your efforts.
We have added a sample design that may help with your submissions. Please see brief
Target Market(s)
early adapters for technology / kestrel, tablet, zorbix users
Requirements
Should not have
- should not be generic design

```html
<!DOCTYPE html>
<html lang="en">
<head>
<meta charset="utf-8">
<title>Video Player App – Results Screen</title>
<link rel="stylesheet" href="https://fonts.googleapis.com/css2?family=Arimo:wght@400;700&display=swap">
<style>
  :root {
    --canvas-bg: #e9ecdc;
    --screen-top: #2c2230;
    --screen-bottom: #1b151d;
    --field-bg: #1a141b;
    --text-main: #ffffff;
    --text-muted: #8d8890;
    --text-body: #e8e6e9;
    --toggle-track: #141014;
    --toggle-knob: #6b6b6b;
    --tabbar-bg: #060506;
    --tab-divider: #242024;
    --icon: #9a9a9a;
  }
  * { box-sizing: border-box; margin: 0; padding: 0; }
  html, body {
    width: 900px; height: 1200px; overflow: hidden;
    background: var(--canvas-bg);
    font-family: "Arimo", Arial, sans-serif;
  }
  .app-screen {
    position: absolute; left: 50px; top: 0;
    width: 800px; height: 1200px; overflow: hidden;
    background: linear-gradient(180deg, var(--screen-top), var(--screen-bottom));
  }
  .brand {
    position: absolute; left: 42px; top: 38px;
    font-size: 50px; font-weight: 700; color: var(--text-main);
    line-height: 1;
  }
  .toggle {
    position: absolute; left: 625px; top: 37px;
    width: 143px; height: 40px; border-radius: 4px;
    background: var(--toggle-track);
  }
  .toggle-knob {
    position: absolute; left: 0; top: 0; width: 70px; height: 40px;
    border-radius: 4px; background: linear-gradient(180deg, #7a7a7a, #555);
    color: var(--text-main); font-size: 18px; font-weight: 700;
    display: flex; align-items: center; justify-content: center;
  }
  .search-field {
    position: absolute; left: 67px; top: 150px;
    width: 663px; height: 87px; border-radius: 6px;
    background: var(--field-bg);
    display: flex; align-items: center; padding-left: 35px;
  }
  .search-placeholder { font-size: 20px; color: var(--text-muted); }
  .search-icon { position: absolute; right: 30px; top: 25px; }
  .results { list-style: none; }
  .result {
    position: absolute; left: 75px; width: 700px; height: 175px;
  }
  .result-thumb {
    position: absolute; left: 0; top: 0; width: 225px; height: 175px;
    border-radius: 10px; box-shadow: 0 0 0 2px rgba(255,255,255,0.08);
  }
  .result-info { position: absolute; left: 275px; top: 12px; width: 430px; }
  .result-title {
    font-size: 22px; font-weight: 700; color: var(--text-main);
    line-height: 30px; margin-bottom: 20px;
  }
  .result-rating { font-weight: 400; }
  .result-desc { font-size: 19px; line-height: 30px; color: var(--text-body); }
  .tab-bar {
    position: absolute; left: 0; top: 1115px; width: 800px; height: 85px;
    background: var(--tabbar-bg); display: flex;
  }
  .tab {
    flex: 1; display: flex; align-items: center; justify-content: center;
    border-left: 2px solid var(--tab-divider);
  }
  .tab:first-child { border-left: none; }
</style>
</head>
<body>
<main class="app-screen">
  <header>
    <div class="brand">Logo</div>
    <div class="toggle" aria-label="Toggle on"><span class="toggle-knob">ON</span></div>
  </header>

  <div class="search-field">
    <span class="search-placeholder">Enter your search here...</span>
    <svg class="search-icon" width="38" height="38" viewBox="0 0 38 38" aria-hidden="true">
      <circle cx="15" cy="15" r="10" fill="none" stroke="#fff" stroke-width="4"/>
      <line x1="22.5" y1="22.5" x2="33" y2="33" stroke="#fff" stroke-width="5" stroke-linecap="round"/>
    </svg>
  </div>

  <ul class="results">
    <li class="result" style="top:287px">
      <div class="result-thumb" role="img" aria-label="Poster still of a romantic comedy film" style="background:linear-gradient(135deg,#c9a48c,#5a6e86 55%,#8a3a3a)"></div>
      <div class="result-info">
        <h2 class="result-title">Echoes of<br>Summers Past</h2>
        <p class="result-desc">Lorem ipsum dolor sit amet, consectetur adipisicing elit, sed do eiusmod tempor incid-idunt</p>
      </div>
    </li>
    <li class="result" style="top:492px">
      <div class="result-thumb" role="img" aria-label="Poster still of a medical drama series" style="background:linear-gradient(135deg,#b9bcc0,#6f6a66 55%,#3c3a3a)"></div>
      <div class="result-info">
        <h2 class="result-title">Doctor Hollow</h2>
        <p class="result-desc">Lorem ipsum dolor sit amet, consectetur adipisicing elit, sed do eiusmod tempor incid-idunt</p>
      </div>
    </li>
    <li class="result" style="top:695px">
      <div class="result-thumb" role="img" aria-label="Poster still of a crime drama series" style="background:linear-gradient(135deg,#9cc3d6,#d9b3a0 50%,#b84a44)"></div>
      <div class="result-info">
        <h2 class="result-title">Baxter IV <span class="result-rating">(12)</span></h2>
        <p class="result-desc">Lorem ipsum dolor sit amet, consectetur adipisicing elit, sed do eiusmod tempor incid-idunt</p>
      </div>
    </li>
    <li class="result" style="top:900px">
      <div class="result-thumb" role="img" aria-label="Poster still of a crime drama series, second season" style="background:linear-gradient(160deg,#2f93ad,#8fc4cf 50%,#d6c2b4)"></div>
      <div class="result-info">
        <h2 class="result-title">Baxter IV <span class="result-rating">(12)</span></h2>
        <p class="result-desc">Lorem ipsum dolor sit amet, consectetur adipisicing elit, sed do eiusmod tempor incid-idunt</p>
      </div>
    </li>
  </ul>

  <nav class="tab-bar">
    <div class="tab" aria-label="TV">
      <svg width="56" height="46" viewBox="0 0 56 46" aria-hidden="true">
        <line x1="22" y1="4" x2="28" y2="12" stroke="var(--icon)" stroke-width="3"/>
        <line x1="36" y1="2" x2="28" y2="12" stroke="var(--icon)" stroke-width="3"/>
        <rect x="4" y="12" width="48" height="30" rx="3" fill="none" stroke="var(--icon)" stroke-width="3"/>
        <rect x="10" y="17" width="30" height="20" fill="#3a3a3a"/>
        <circle cx="46" cy="22" r="2" fill="var(--icon)"/>
        <circle cx="46" cy="30" r="2" fill="var(--icon)"/>
      </svg>
    </div>
    <div class="tab" aria-label="History">
      <svg width="48" height="48" viewBox="0 0 48 48" aria-hidden="true">
        <circle cx="24" cy="24" r="20" fill="#3a3a3a" stroke="var(--icon)" stroke-width="3"/>
        <path d="M24 12v13h9" fill="none" stroke="#ddd" stroke-width="3" stroke-linecap="round"/>
      </svg>
    </div>
    <div class="tab" aria-label="Search">
      <svg width="46" height="46" viewBox="0 0 46 46" aria-hidden="true">
        <circle cx="18" cy="18" r="12" fill="none" stroke="var(--icon)" stroke-width="4"/>
        <line x1="27" y1="27" x2="40" y2="40" stroke="var(--icon)" stroke-width="6" stroke-linecap="round"/>
      </svg>
    </div>
    <div class="tab" aria-label="Favourites">
      <svg width="50" height="48" viewBox="0 0 50 48" aria-hidden="true">
        <polygon points="25,3 31,18 47,18 34,28 39,44 25,34 11,44 16,28 3,18 19,18" fill="var(--icon)"/>
      </svg>
    </div>
    <div class="tab" aria-label="More">
      <svg width="70" height="20" viewBox="0 0 70 20" aria-hidden="true">
        <circle cx="10" cy="10" r="8" fill="var(--icon)"/>
        <circle cx="35" cy="10" r="8" fill="var(--icon)"/>
        <circle cx="60" cy="10" r="8" fill="var(--icon)"/>
      </svg>
    </div>
  </nav>
</main>
</body>
</html>
```